Pelican Litigation Funding Letterhead & Document Template

We need a letter head designed for our fund. Our fund works with law firms and investors across the globe. We need a a cover letter template as well as a document template for subsequent pages. Blue and white color scheme is preferred. This is our predecessor's website: https://www.pelicanvq.com/index.html. Please see our logo attached. The logo color code is #19478d. Font is Gotham-Medium.
Target Market(s)
Sophisticated investors and law firms
Font styles to use
Sans Serif
Colors
0255a3

```html
<!DOCTYPE html>
<html lang="en">
<head>
<meta charset="utf-8">
<title>Pelican Litigation Funding — Letterhead</title>
<link rel="stylesheet" href="https://fonts.googleapis.com/css2?family=Montserrat:wght@400;500;600&display=swap">
<style>
  :root{
    --brand-blue:#19478d;
    --accent-gray:#c3c4c7;
    --faint-gray:#f6f6f7;
    --ink-dark:#333539;
    --ink-body:#707276;
    --ink-footer:#55575b;
    --paper:#ffffff;
  }
  *{margin:0;padding:0;box-sizing:border-box}
  html,body{width:846px;height:1200px;overflow:hidden;background:var(--paper)}
  body{font-family:"Montserrat",sans-serif;color:var(--ink-body)}
  .letterhead{position:relative;width:846px;height:1200px;background:var(--paper);overflow:hidden}
  .page-shapes{position:absolute;inset:0;width:846px;height:1200px}
  .brand{position:absolute;left:93px;top:150px;width:305px;text-align:center;color:var(--brand-blue);font-size:19px;font-weight:500;line-height:1;white-space:nowrap}
  .sender{position:absolute;left:81px;top:236px}
  .sender-name{font-size:26px;font-weight:500;color:var(--ink-dark);line-height:1.1}
  .sender-role{font-size:14px;font-weight:500;margin-top:2px}
  .contact{position:absolute;left:81px;top:307px;font-size:14.5px;font-weight:500;line-height:25px}
  .contact-row{display:flex}
  .contact-label{width:67px}
  .contact-sep{width:15px}
  .letter-body{position:absolute;left:81px;top:445px;width:704px;font-size:14.9px;font-weight:500;line-height:25px;hyphens:auto;-webkit-hyphens:auto}
  .letter-body p+p{margin-top:25px}
  .signature{position:absolute;left:81px;top:912px;width:170px;height:24px;background:linear-gradient(90deg,#3a3a3a22,#3a3a3a08)}
  .signoff-name{position:absolute;left:81px;top:952px;font-size:26px;font-weight:500;color:var(--ink-dark)}
  .footer-contact{position:absolute;left:420px;top:1088px;font-size:13px;color:var(--ink-footer);line-height:24.5px}
  .footer-row{display:flex;align-items:center;gap:8px}
  .footer-row svg{width:12px;height:12px;flex:none}
</style>
</head>
<body>
<main class="letterhead">
  <svg class="page-shapes" viewBox="0 0 932 1318" preserveAspectRatio="none" aria-hidden="true">
    <polygon fill="var(--faint-gray)" points="520,1318 932,560 932,650 600,1318"/>
    <polygon fill="var(--faint-gray)" points="640,1318 932,770 932,860 720,1318"/>
    <polygon fill="var(--brand-blue)" points="0,0 252,0 0,182"/>
    <polygon fill="var(--accent-gray)" points="0,190 232,30 0,210"/>
    <polygon fill="var(--brand-blue)" points="265,0 932,0 932,185"/>
    <polygon fill="var(--accent-gray)" points="300,14 862,168 828,202"/>
    <polygon fill="var(--accent-gray)" points="2,1140 405,1285 2,1168"/>
    <polygon fill="var(--brand-blue)" points="2,1187 480,1318 2,1318"/>
  </svg>

  <header class="brand">Pelican Litigation Funding</header>

  <section class="sender">
    <h1 class="sender-name">Jon K</h1>
    <div class="sender-role">Creative Designer</div>
  </section>

  <section class="contact">
    <div class="contact-row"><span class="contact-label">Address</span><span class="contact-sep">:</span><span>xygjkl 55 neywork, United Stated-450</span></div>
    <div class="contact-row"><span class="contact-label">Email</span><span class="contact-sep">:</span><span>pelicanlitigation@gmail.com</span></div>
    <div class="contact-row"><span class="contact-label">Web</span><span class="contact-sep">:</span><span>www.pelicanlitigation.com</span></div>
    <div class="contact-row"><span class="contact-label">Phone</span><span class="contact-sep">:</span><span>+1 01236 45466590</span></div>
  </section>

  <article class="letter-body">
    <p>Lorem ipsum dolor sit amet, consectetur adipiscing elit. Praesent suscipit vitae sapien ut imperdiet. Duis lobortis tellus eu condimentum bibendum. Suspendisse purus arcu, tincidunt vitae sodales et, vulputate non tortor. Mauris nulla ipsum, fringilla ac mauris quis, vestibulum bibendum metus. Suspendisse sodales ultricies pulvinar. In tempor ligula vel eleifend volutpat.</p>
    <p>In consequat a nibh ut dapibus. Nullam et interdum lorem. Cras arcu nisl, tincidunt non efficitur nec, faucibus nec enim. Curabitur a lectus sed nunc ultricies molestie non ac elit. Donec sed dolor sed nisi interdum pulvinar non eu ligula. Proin sollicitudin neque vel felis elementum congue. Praesent eu tortor ut augue posuere condimentum. In molestie dapibus est at viverra. Integer vulputate mauris nec luctus dignissim. Fusce mattis vehicula auctor.</p>
    <p>In consequat a nibh ut dapibus. Nullam et interdum lorem. Cras arcu nisl, tincidunt non efficitur nec, faucibus nec enim. Curabitur a lectus sed nunc ultricies molestie non ac elit. Donec sed dolor sed nisi interdum pulvinar non eu ligula.</p>
  </article>

  <div class="signature" role="img" aria-label="Handwritten signature"></div>
  <div class="signoff-name">Jon K</div>

  <footer class="footer-contact">
    <div class="footer-row">
      <svg viewBox="0 0 12 12"><circle cx="6" cy="6" r="5" fill="none" stroke="currentColor" stroke-width="1.4"/><path d="M4 3.5l1 1-.6.9a4 4 0 0 0 2.2 2.2l.9-.6 1 1-.8.8C5.6 8.6 3.4 6.4 3.2 4.3z" fill="currentColor"/></svg>
      <span>+012 34567 8999 &nbsp;|&nbsp; +012 00112 8999</span>
    </div>
    <div class="footer-row">
      <svg viewBox="0 0 12 12"><circle cx="6" cy="6" r="5" fill="none" stroke="currentColor" stroke-width="1.4"/><circle cx="6" cy="6" r="2.2" fill="currentColor"/></svg>
      <span>hereyour@mailid.com &nbsp;|&nbsp; www.yourwebsite.com</span>
    </div>
    <div class="footer-row">
      <svg viewBox="0 0 12 12"><circle cx="6" cy="6" r="5" fill="none" stroke="currentColor" stroke-width="1.4"/><circle cx="6" cy="6" r="2.2" fill="currentColor"/></svg>
      <span>Here Your Address, 555 Newyourk, United State-500</span>
    </div>
  </footer>
</main>
</body>
</html>
```